Business Card Design

We need a business card that reflects a company that has been established for over 20 years, a card that displays confidence.
Although we are established we are forward thinking and always pushing forward.
Our company buys, processes and exports scrap metal all over the world.
We buy metal from all around Australia, although we sell it all across the globe.
The card should look modern, bold, but not over complicated.
Incorporate the Logo and the company colors.
Would like to see in raised lettering.
Updates

Thank you to all designers, same amazing designs in such a short time.

At this stage designer Lumosh is the front runner.
The design is crisp, clean and modern, not to busy.
I would like to see what you all come up with in the next 24 hours.
Thank you

Industry/Entity Type

Business

Contact Information for Business Card

Dravik Metal Recyclers
Owen Strazdins
Director
4-8 Corvane Road
Kestrel Flats, Northvale 5990
Phone +61-8-8374-2619
Fax +61-8-8374 5102
Mobile 0412 395 860
email: owen@dravik.example.au
web: www.dravik.example.au

```html
<!DOCTYPE html>
<html lang="en">
<head>
<meta charset="utf-8">
<title>Dravik Metal Recyclers – Business Card</title>
<link href="https://fonts.googleapis.com/css2?family=Questrial&display=swap" rel="stylesheet">
<style>
  :root {
    --page-bg: #e6e6e6;
    --card-bg: #ffffff;
    --ink: #2b2b2b;
    --green: #3f8a35;
    --rule: #555555;
  }
  * { margin: 0; padding: 0; box-sizing: border-box; }
  html, body {
    width: 1200px; height: 900px; overflow: hidden;
    background: var(--page-bg);
    font-family: "Questrial", "Century Gothic", sans-serif;
    color: var(--ink);
  }
  .canvas {
    position: relative; width: 1200px; height: 900px;
    display: flex; align-items: center; justify-content: center;
  }
  .business-card {
    position: relative;
    width: 900px; height: 515px;
    background: var(--card-bg);
    box-shadow: 0 6px 22px rgba(0,0,0,0.12);
    display: flex; align-items: center;
  }
  .brand {
    width: 430px; padding-left: 70px;
    display: flex; align-items: center; gap: 18px;
  }
  .brand-dot {
    width: 44px; height: 44px; border-radius: 50%;
    background: var(--green); flex: none;
  }
  .brand-name {
    font-size: 34px; line-height: 1.15; color: var(--ink);
    letter-spacing: 0.5px;
  }
  .divider {
    width: 2px; height: 290px; background: var(--rule);
    margin-right: 38px;
  }
  .contact { display: flex; flex-direction: column; }
  .person-name { font-size: 29px; line-height: 1.05; }
  .person-role { font-size: 29px; line-height: 1.05; color: var(--green); margin-bottom: 26px; }
  .contact-list { list-style: none; }
  .contact-item {
    display: flex; align-items: flex-start; gap: 14px;
    font-size: 21px; line-height: 26px; margin-bottom: 12px;
  }
  .contact-icon { width: 26px; height: 26px; flex: none; }
  .contact-icon circle.ring { fill: none; stroke: var(--green); stroke-width: 1.6; }
  .contact-icon .glyph { fill: none; stroke: var(--green); stroke-width: 1.6; stroke-linecap: round; stroke-linejoin: round; }
  .contact-icon .solid { fill: var(--green); }
</style>
</head>
<body>
<main class="canvas">
  <section class="business-card">
    <div class="brand">
      <span class="brand-dot" aria-hidden="true"></span>
      <span class="brand-name">Dravik Metal<br>Recyclers</span>
    </div>
    <div class="divider" aria-hidden="true"></div>
    <div class="contact">
      <p class="person-name">Owen Strazdins</p>
      <p class="person-role">Director</p>
      <ul class="contact-list">
        <li class="contact-item">
          <svg class="contact-icon" viewBox="0 0 26 26" aria-label="Mobile"><circle class="ring" cx="13" cy="13" r="11.5"/><rect class="glyph" x="9.5" y="6.5" width="7" height="13" rx="1.2"/><line class="glyph" x1="12" y1="17" x2="14" y2="17"/></svg>
          <span>0412 395 860</span>
        </li>
        <li class="contact-item">
          <svg class="contact-icon" viewBox="0 0 26 26" aria-label="Phone"><circle class="ring" cx="13" cy="13" r="11.5"/><path class="glyph" d="M9 7l2.5 0 1 3-1.6 1.2a7 7 0 0 0 3.9 3.9L16 13.5l3 1v2.5c0 1-1 1.5-2 1.3A10 10 0 0 1 7.7 9c-.2-1 .3-2 1.3-2z"/></svg>
          <span>+61-8-8374-2619</span>
        </li>
        <li class="contact-item">
          <svg class="contact-icon" viewBox="0 0 26 26" aria-label="Fax"><circle class="ring" cx="13" cy="13" r="11.5"/><rect class="glyph" x="7" y="11" width="12" height="7" rx="1"/><rect class="glyph" x="9.5" y="6.5" width="7" height="4.5"/><line class="glyph" x1="9.5" y1="15" x2="16.5" y2="15"/></svg>
          <span>+61-8-8374 5102</span>
        </li>
        <li class="contact-item">
          <svg class="contact-icon" viewBox="0 0 26 26" aria-label="Website"><circle class="ring" cx="13" cy="13" r="11.5"/><circle class="glyph" cx="13" cy="13" r="7"/><ellipse class="glyph" cx="13" cy="13" rx="3" ry="7"/><line class="glyph" x1="6" y1="13" x2="20" y2="13"/></svg>
          <span>www.dravik.example.au</span>
        </li>
        <li class="contact-item">
          <svg class="contact-icon" viewBox="0 0 26 26" aria-label="Email"><circle class="ring" cx="13" cy="13" r="11.5"/><rect class="glyph" x="7" y="8.5" width="12" height="9" rx="1"/><path class="glyph" d="M7 9l6 5 6-5"/></svg>
          <span>owen@dravik.example.au</span>
        </li>
        <li class="contact-item">
          <svg class="contact-icon" viewBox="0 0 26 26" aria-label="Address"><circle class="ring" cx="13" cy="13" r="11.5"/><path class="solid" d="M13 5.5a5 5 0 0 0-5 5c0 3.6 5 9.5 5 9.5s5-5.9 5-9.5a5 5 0 0 0-5-5z"/><circle cx="13" cy="10.5" r="1.8" fill="#fff"/></svg>
          <span>4-8 Corvane Road Kestrel Flats,<br>Northvale 5990</span>
        </li>
      </ul>
    </div>
  </section>
</main>
</body>
</html>
```